Rlm Pavora Broth is looking for a DL Flyer for their unique food the #tindelbroth

We're looking for a punchy flyer which depicts our food dish and includes a small blurb on the front & back. Flyer size is portrait style DL (210 x 99mm) & must be 'Press Ready Files'.
Brief: Flyer background is light wooden chopping board with vertical strips.

(Text: Calibri Body or similar text, must be easy to read! Minimum 50% width)
Rlm proudly present..
(Text: Calibri Body Header or similar text, must be easy to read! Min. 75% width) PAVORA BROTH

Below the text PAVORA BROTH insert an image (size is approx 25% of Flyer) of Borneo with a reference to Kuching. Map of Borneo can be an outline or similar but not too prominent.
Overlay the top of the map with the following text in Monotype Corsivab or similar! but must be easy to read.
Text: Kuching (2 sizes larger) Capital City of Sarawak on the Island of Borneo is home to some of the world’s greatest and unique dishes.
(new line) Rlm will take you on a culinary journey to Kuching with a favourite local dish the
(new line) #TindelBroth (double space) so sit back, relax & enjoy!

Insert and centre the attached image DSC_0927.JPG
Remove the spoon and make the image more vibrant, do not change the colour of the soup.
Refer to attached file Flyer.jpg for images of chopsticks, a boiled egg and ingredients at the bottom. We like the lines to point to key ingredients e.g. to the egg, prawns etc. current design the font is difficult to read.

List contact details toward the bottom.
e: Rlm.PavoraBroth@quellmail.test
m: +61 438207519
f : Rlm Pavora Broth

on the reverse of the Flyer:
Background is light wooden chopping board with vertical strips, same as front.

Refer to below link for text & Nutritional Values table.
The text for the main four paragraphs should be the key note and majority.
Note the Ingredients and the Nutritional Values table size is max 12.5% of the total Flyer size.

https://files.veltrodocs.test/doc/7QmRz3pLx9KwT2vNc8YhB4sD6fGj1aE0uI5oZkXnWq/edit?share=open

Target Market(s)

An international foody with a sense of adventure. The dish is nutritional, Gluten Free and a healthy meal. It will be sold at food markets, to office workers for lunch and for a lighter evening meal.

Industry/Entity Type

Food Production

Colors

Designer to choose colors to be used in the design.

Requirements
Must have
• 'Rlm proudly present..' must be a statement along with the product 'PAVORA BROTH'
• The map of Borneo with reference to Kuching, the home of the product.
• A picture of the dish itself.

```html
<!DOCTYPE html>
<html lang="en">
<head>
<meta charset="utf-8">
<title>Pavora Broth DL Flyer</title>
<link rel="stylesheet" href="https://fonts.googleapis.com/css2?family=Carlito:ital,wght@0,400;0,700;1,400&family=Cormorant+Garamond:ital,wght@1,500;1,600&family=Open+Sans:wght@600;700&display=swap">
<style>
  :root {
    --backdrop: #d9a612;
    --wood-light: #f1f1f0;
    --wood-mid: #e2e2e1;
    --wood-line: #cfcfcd;
    --accent: #f05a22;
    --ink: #1f1f1f;
    --ink-soft: #333;
    --rule: #9a9a9a;
    --table-line: #b5b5b5;
  }
  * { box-sizing: border-box; margin: 0; padding: 0; }
  html, body { width: 1200px; height: 1200px; overflow: hidden; }
  body {
    background: var(--backdrop);
    position: relative;
    font-family: "Carlito", "Calibri", sans-serif;
    color: var(--ink);
  }
  .flyer {
    position: absolute;
    top: 176px;
    height: 870px;
    overflow: hidden;
    background:
      repeating-linear-gradient(90deg,
        transparent 0 58px,
        var(--wood-line) 58px 60px,
        transparent 60px 118px),
      repeating-linear-gradient(90deg,
        var(--wood-light) 0 30px,
        var(--wood-mid) 30px 34px,
        var(--wood-light) 34px 80px);
  }
  .flyer--front { left: 126px; width: 480px; }
  .flyer--back { left: 647px; width: 446px; }
  .abs { position: absolute; }

  /* front */
  .product-title {
    left: 48px; top: 40px;
    font-family: "Open Sans", sans-serif;
    font-weight: 700;
    font-size: 47px;
    letter-spacing: 1px;
    color: var(--accent);
    white-space: nowrap;
  }
  .intro {
    left: 49px; width: 392px;
    font-family: "Cormorant Garamond", serif;
    font-style: italic;
    font-weight: 500;
    font-size: 14px;
    line-height: 17px;
    color: var(--ink-soft);
  }
  .intro--place { top: 114px; text-align: justify; }
  .intro--place .place-name {
    font-family: "Carlito", sans-serif;
    font-style: normal;
    font-weight: 700;
    font-size: 19px;
    color: var(--ink);
  }
  .intro--journey { top: 170px; width: 390px; }
  .intro--tag { top: 219px; left: 54px; width: 260px; }
  .map-area {
    left: 312px; top: 186px; width: 126px; height: 102px;
    border-radius: 40% 55% 35% 50%;
    background: linear-gradient(160deg, #e6ebe6, #d3dad3);
  }
  .dish-photo {
    left: 56px; top: 312px; width: 370px; height: 316px;
    border-radius: 50%;
    background: radial-gradient(circle at 50% 50%, #b5552e 0 34%, #d99a6a 48%, #f4f4f4 60%, #ffffff 70%);
  }
  .chopsticks {
    left: 418px; top: 308px; width: 62px; height: 316px;
    background: linear-gradient(100deg, transparent 30%, #dcb27a 40%, #c79a5f 55%, transparent 65%);
  }
  .callouts { left: 0; top: 0; width: 480px; height: 870px; pointer-events: none; }
  .callout {
    font-family: "Cormorant Garamond", serif;
    font-style: italic;
    font-weight: 600;
    font-size: 18px;
    line-height: 16px;
    color: var(--ink-soft);
    white-space: nowrap;
  }
  .callout--chicken { left: 63px; top: 296px; }
  .callout--prawns { left: 204px; top: 277px; }
  .callout--egg { left: 90px; top: 635px; }
  .callout--beancurd { left: 342px; top: 603px; text-align: right; }
  .contact-rule { left: 90px; top: 698px; width: 328px; height: 1px; background: var(--rule); }
  .contacts {
    left: 98px; top: 706px;
    list-style: none;
    font-family: "Open Sans", sans-serif;
    font-weight: 600;
    font-size: 17px;
    color: #333;
  }
  .contacts li { display: flex; align-items: center; height: 24px; gap: 9px; }
  .contacts svg { width: 17px; height: 17px; flex: none; }
  .herb-right {
    left: 432px; top: 648px; width: 48px; height: 100px;
    border-radius: 60% 0 0 60%;
    background: linear-gradient(135deg, #5aa33a, #2f7a24);
  }
  .asparagus {
    left: 0; top: 440px; width: 60px; height: 430px;
    background: linear-gradient(90deg, #8fb84a, #c6dc7c 50%, #9bc055);
  }
  .basil-left {
    left: 0; top: 544px; width: 70px; height: 104px;
    border-radius: 0 60% 60% 0;
    background: linear-gradient(135deg, #4c9b30, #2d6f1f);
  }
  .ingredients-band {
    left: 60px; top: 800px; width: 420px; height: 70px;
    background: linear-gradient(90deg, #c9954e 0 30%, #9e2a1d 45%, #b83a22 62%, #efe4d6 78%, #f4ece2);
  }

  /* back */
  .story {
    left: 41px; width: 364px;
    font-size: 14.2px;
    line-height: 17px;
    text-align: justify;
    color: var(--ink);
  }
  .story .hl { color: var(--accent); font-weight: 400; }
  .story b { font-weight: 700; }
  .story--1 { top: 57px; }
  .story--2 { top: 125px; }
  .story--3 { top: 210px; }
  .story--4 { top: 278px; }
  .story--5 { top: 380px; }
  .story--6 { top: 432px; }
  .story--ingredients { top: 517px; }
  .story--ingredients i { font-style: italic; }
  .nutrition {
    left: 41px; top: 624px; width: 364px;
    border-collapse: collapse;
    font-family: "Open Sans", sans-serif;
    font-size: 13px;
    background: rgba(255,255,255,0.35);
  }
  .nutrition th {
    background: var(--accent);
    color: var(--ink);
    font-weight: 600;
    text-align: left;
    vertical-align: top;
    padding: 4px 10px 4px 11px;
    height: 40px;
    line-height: 16px;
    border: 1px solid #c44a1c;
  }
  .nutrition td {
    border: 1px solid var(--table-line);
    border-top: none;
    height: 23px;
    padding: 0 10px;
    font-weight: 600;
  }
  .nutrition td.value {
    font-family: "Carlito", sans-serif;
    font-weight: 400;
    font-size: 15px;
    padding-left: 38px;
  }
  .nutrition td.sub { padding-left: 100px; }
  .nutrition col.label { width: 218px; }
  .nutrition tr.first td { padding-top: 6px; height: 29px; }
  .chillies-back {
    left: 0; top: 820px; width: 72px; height: 50px;
    background: linear-gradient(120deg, #a82c1c, #6e1a12);
    border-radius: 0 50% 0 0;
  }
  .basil-back {
    left: 350px; top: 800px; width: 96px; height: 70px;
    border-radius: 60% 0 0 0;
    background: linear-gradient(135deg, #5aa33a, #2f7a24);
  }
</style>
</head>
<body>

<section class="flyer flyer--front">
  <h1 class="abs product-title">PAVORA BROTH</h1>

  <p class="abs intro intro--place"><span class="place-name">Kuching</span> Capital City of Sarawak on the Island of Borneo is home to some of the world’s greatest and unique dishes.</p>
  <p class="abs intro intro--journey">Rlm will take you on a culinary journey to Kuching with a favourite local dish the</p>
  <p class="abs intro intro--tag">#TindelBroth&nbsp; so sit back, relax &amp; enjoy!</p>

  <div class="abs map-area" role="img" aria-label="Outline map of Borneo with a pin marking Kuching"></div>

  <div class="abs chopsticks" role="img" aria-label="Pair of wooden chopsticks"></div>
  <div class="abs dish-photo" role="img" aria-label="Bowl of broth with rice vermicelli, chicken strips, king prawns, omelette strips, fried bean curd and half a boiled egg"></div>

  <svg class="abs callouts" viewBox="0 0 480 870" aria-hidden="true">
    <g stroke="#555" stroke-width="0.8" fill="none">
      <line x1="118" y1="316" x2="146" y2="400"/>
      <line x1="245" y1="298" x2="242" y2="432"/>
      <line x1="146" y1="632" x2="182" y2="572"/>
      <line x1="378" y1="604" x2="362" y2="512"/>
    </g>
  </svg>
  <span class="abs callout callout--chicken">Chicken breast</span>
  <span class="abs callout callout--prawns">King Prawns</span>
  <span class="abs callout callout--egg">Free Range Egg</span>
  <span class="abs callout callout--beancurd">Fried bean<br>curd</span>

  <div class="abs herb-right" role="img" aria-label="Fresh basil leaves"></div>
  <div class="abs basil-left" role="img" aria-label="Fresh basil leaves"></div>
  <div class="abs asparagus" role="img" aria-label="Green asparagus spears"></div>

  <div class="abs contact-rule"></div>
  <ul class="abs contacts">
    <li>
      <svg viewBox="0 0 16 16" aria-hidden="true"><rect x="1" y="3.5" width="14" height="9" fill="#222"/><path d="M1 3.5 8 9 15 3.5" stroke="#fff" stroke-width="1.2" fill="none"/></svg>
      Rlm.PavoraBroth@quellmail.test
    </li>
    <li>
      <svg viewBox="0 0 16 16" aria-hidden="true"><rect x="1" y="1" width="14" height="14" rx="3" fill="#222"/><path d="M5 4c-.6.6-.8 1.6-.2 3 .9 2 2.3 3.5 4.3 4.4 1.3.6 2.3.4 2.9-.2l-1.6-1.6-1.3.6C8.1 9.6 6.9 8.4 6.3 7.3l.6-1.3z" fill="#fff"/></svg>
      +61 438207519
    </li>
    <li>
      <svg viewBox="0 0 16 16" aria-hidden="true"><circle cx="8" cy="8" r="6.5" fill="none" stroke="#222" stroke-width="1.3"/></svg>
      Rlm Pavora Broth
    </li>
  </ul>

  <div class="abs ingredients-band" role="img" aria-label="Fresh ginger root, dried red chillies and garlic bulbs"></div>
</section>

<section class="flyer flyer--back">
  <p class="abs story story--1"><span class="hl">Roving Plates:</span> a short while ago on my travels around East Malaysia I was introduced to a place called Kuching, Capital City of Sarawak.</p>
  <p class="abs story story--2">I was overwhelmed by their number of unique dishes, from the Sea to the Borneo Jungle local sustainable ingredients are sourced to create some of Kuching’s indigenous foods.</p>
  <p class="abs story story--3">I was astonished to learn that famous Kuching dishes like Kolo Mee and the Tindel Broth are breakfast dishes and often sold out by 10am.</p>
  <p class="abs story story--4">I have chosen the <span class="hl">Tindel Broth</span> to share with You...<br>It converts perfectly to our requirements - a healthy, <b>Gluten-Free</b> nourishing meal, although maybe not breakfast for everyone!</p>
  <p class="abs story story--5"><span class="hl">The Laksa sambal</span> / base stock is made from ALL plant-based ingredients.</p>
  <p class="abs story story--6">We add a dash of coconut milk to bring balance to this simple yet complex dish; with it’s more subtle and fine blend of aromatic herbs and spices and a hint of sour and chilli undertones.</p>
  <p class="abs story story--ingredients"><b>Ingredients:</b> <i>rice vermicelli - bihoon, omelette strips (free range eggs), sliced chicken breast, King prawns, bean-sprouts, fried bean curd and garnished with lime wedge, fresh coriander and sambal on the side.</i></p>

  <table class="abs nutrition">
    <colgroup><col class="label"><col></colgroup>
    <thead>
      <tr><th>NUTRITION INFORMATION:</th><th>Pavora Broth<br>Per serve</th></tr>
    </thead>
    <tbody>
      <tr class="first"><td>ENERGY</td><td class="value">1920 kj</td></tr>
      <tr><td>CALORIES</td><td class="value">458</td></tr>
      <tr><td>PROTEIN</td><td class="value">30g</td></tr>
      <tr><td class="sub">-GLUTEN</td><td class="value">UNDETECTED</td></tr>
      <tr><td>FAT - TOTAL</td><td class="value">38g</td></tr>
      <tr><td>CARBOHYDRATES</td><td class="value">52g</td></tr>
    </tbody>
  </table>

  <div class="abs chillies-back" role="img" aria-label="Dried red chillies"></div>
  <div class="abs basil-back" role="img" aria-label="Fresh basil leaves"></div>
</section>

</body>
</html>
```